International Medical travel company needs professional card

We just purchased a logo through sketch nest, and now need a business card. We contract with Middle Eastern governments to bring patients who need complex medical care to the U.S. for treatment. We will upload logo. Titles, names, contact info, etc. needs to be in English on one side, Arabic on the other

Target Market(s)

Health administrators, professionals

Industry/Entity Type

Health Care

Contact Information for Business Card

logo on each side. Usual name/title/contact info

Font styles to use
Serif
Sans Serif

Colors
0255a3

Requirements
Must have
• English one side, Arabic the other

```html
<!DOCTYPE html>
<html lang="en">
<head>
<meta charset="utf-8">
<title>Meridian Care – Business Card</title>
<link rel="stylesheet" href="https://fonts.googleapis.com/css2?family=EB+Garamond:wght@400;600;700&family=Noto+Naskh+Arabic:wght@400;700&display=swap">
<style>
  :root {
    --page: #2a2a2c;
    --card-white: #f7f8f9;
    --brand-blue: #0255a3;
    --blue-deep: #0a4a8e;
    --ink-navy: #0b2346;
    --gold: #b3a31e;
    --light-text: #e6edf5;
    --muted: #5a6470;
  }
  * { box-sizing: border-box; margin: 0; padding: 0; }
  html, body { width: 1200px; height: 873px; overflow: hidden; }
  body {
    background: var(--page);
    font-family: "EB Garamond", Georgia, serif;
    position: relative;
  }
  .card {
    position: absolute;
    width: 600px;
    height: 343px;
    border-radius: 16px;
    overflow: hidden;
    background: var(--card-white);
    box-shadow: 0 14px 30px rgba(0,0,0,.45);
  }
  .card--arabic { left: 90px; top: 70px; }
  .card--english { left: 510px; top: 460px; }

  /* blue band with stripe rules */
  .band {
    position: absolute;
    left: 0; right: 0;
    background: var(--brand-blue);
  }
  .rule {
    position: absolute;
    left: 0; right: 0;
    background: var(--brand-blue);
  }

  /* English side */
  .card--english .rule--thin { top: 132px; height: 2px; }
  .card--english .rule--mid { top: 138px; height: 4px; }
  .card--english .band { top: 147px; bottom: 0; }

  .brand {
    position: absolute;
    display: flex;
    align-items: center;
    gap: 12px;
  }
  .brand__mark {
    width: 30px; height: 30px;
    border: 3px solid currentColor;
  }
  .brand__name {
    font-family: "EB Garamond", Georgia, serif;
    font-weight: 600;
    font-size: 38px;
    letter-spacing: 1px;
    line-height: 1;
  }
  .card--english .brand { left: 0; right: 0; top: 44px; justify-content: center; color: var(--gold); }

  .person {
    position: absolute;
    text-align: center;
  }
  .card--english .person { left: 40px; width: 260px; top: 188px; }
  .person__name { font-size: 22px; font-weight: 600; color: var(--light-text); }
  .person__title { font-size: 18px; color: var(--light-text); margin-top: 2px; }
  .person__address {
    font-size: 17px; font-weight: 700; color: var(--ink-navy);
    margin-top: 22px; line-height: 1.25;
  }

  .divider {
    position: absolute;
    width: 2px;
    background: linear-gradient(to bottom, rgba(255,255,255,0), rgba(255,255,255,.9), rgba(255,255,255,0));
  }
  .card--english .divider { left: 318px; top: 180px; height: 120px; }

  .contacts {
    position: absolute;
    list-style: none;
  }
  .contacts li {
    display: flex; align-items: center; gap: 10px;
    font-size: 17px; font-weight: 700; color: var(--ink-navy);
    line-height: 1.5;
  }
  .contacts svg { width: 16px; height: 16px; flex: none; }
  .card--english .contacts { left: 346px; top: 186px; }
  .card--english .contacts svg { fill: var(--ink-navy); }

  /* Arabic side */
  .card--arabic .band { top: 224px; bottom: 0; }
  .card--arabic .rule--thin { top: 210px; height: 2px; }
  .card--arabic .rule--mid { top: 216px; height: 4px; }
  .card--arabic .brand { left: 0; right: 0; top: 262px; justify-content: center; color: var(--card-white); }
  .card--arabic .brand__name { font-size: 42px; }

  .person--arabic {
    font-family: "Noto Naskh Arabic", "EB Garamond", serif;
    right: 36px; top: 34px; width: 260px; text-align: right;
  }
  .person--arabic .person__name { color: var(--gold); font-size: 26px; font-weight: 700; }
  .person--arabic .person__title { color: var(--muted); font-size: 15px; }
  .person--arabic .person__address { color: var(--ink-navy); font-size: 16px; font-weight: 700; margin-top: 14px; line-height: 1.45; }

  .card--arabic .divider {
    left: 300px; top: 40px; height: 130px;
    background: linear-gradient(to bottom, rgba(2,85,163,0), rgba(2,85,163,.8), rgba(2,85,163,0));
  }
  .card--arabic .contacts { left: 60px; top: 50px; }
  .card--arabic .contacts li { font-size: 15px; font-weight: 400; color: var(--muted); }
  .card--arabic .contacts svg { fill: var(--gold); }
</style>
</head>
<body>

  <svg width="0" height="0" style="position:absolute" aria-hidden="true">
    <symbol id="icon-phone" viewBox="0 0 16 16"><path d="M2 5c0-2 3-3 6-3s6 1 6 3v1h-3V5H5v1H2zM4 8h8l2 6H2z"/></symbol>
    <symbol id="icon-mobile" viewBox="0 0 16 16"><path d="M4 1h8v14H4zM5.5 2.5v10h5v-10z"/></symbol>
    <symbol id="icon-fax" viewBox="0 0 16 16"><path d="M4 1h8v4H4zM1 6h14v6h-3v3H4v-3H1zM5 10v4h6v-4z"/></symbol>
    <symbol id="icon-mail" viewBox="0 0 16 16"><path d="M1 3h14v10H1zM2.5 4.5 8 9l5.5-4.5v7h-11z"/></symbol>
  </svg>

  <section class="card card--arabic" lang="ar">
    <div class="person person--arabic" dir="rtl">
      <p class="person__name">صموئيل هارت</p>
      <p class="person__title">المالك / المؤسس</p>
      <p class="person__address">4810 طريق ألدر ريدج ، جناح B<br>فيرفيو ، تكساس 78000</p>
    </div>
    <div class="divider"></div>
    <ul class="contacts" lang="en">
      <li><svg><use href="#icon-phone"/></svg>210-555-0142</li>
      <li><svg><use href="#icon-mobile"/></svg>210-555-0178</li>
      <li><svg><use href="#icon-fax"/></svg>210-555-0193</li>
      <li><svg><use href="#icon-mail"/></svg>info@meridiancare.com</li>
    </ul>
    <div class="rule rule--thin"></div>
    <div class="rule rule--mid"></div>
    <div class="band"></div>
    <div class="brand" lang="en">
      <span class="brand__mark"></span>
      <span class="brand__name">MERIDIAN CARE</span>
    </div>
  </section>

  <section class="card card--english">
    <div class="brand">
      <span class="brand__mark"></span>
      <span class="brand__name">MERIDIAN CARE</span>
    </div>
    <div class="rule rule--thin"></div>
    <div class="rule rule--mid"></div>
    <div class="band"></div>
    <div class="person">
      <p class="person__name">Samuel Hart</p>
      <p class="person__title">Owner / Founder</p>
      <p class="person__address">4810 Alder Ridge Rd., Suite B.<br>Fairview, TX. 78000</p>
    </div>
    <div class="divider"></div>
    <ul class="contacts">
      <li><svg><use href="#icon-phone"/></svg>210-555-0142</li>
      <li><svg><use href="#icon-mobile"/></svg>210-555-0178</li>
      <li><svg><use href="#icon-fax"/></svg>210-555-0193</li>
      <li><svg><use href="#icon-mail"/></svg>info@meridiancare.com</li>
    </ul>
  </section>

</body>
</html>
```